Peanut Butter for Dogs - Label

Dear Designers,

Our company develops natural & innovative products aimed at enhancing animal (cat & dog) well-being. The company focuses on producing high-end, ethically sourced products that naturally soothe pets, improving their quality of life.

We are currently developing a new CBD-enriched Peanut Butter product for dogs, and we are looking for some label designs that follow our brand image & brand identity.

-> Please see full brief PDF file attached.

Target Market(s)

European Market (French Speaking)

Industry/Entity Type

Pet Food

Font styles to use
Other font styles liked:
• Please see brand kit in PDF brief

Colors

Designer to choose colors to be used in the design.

Requirements
Must have
• Please see brief PDF file attached
Nice to have
Should not have

```html
<!DOCTYPE html>
<html lang="fr">
<head>
<meta charset="UTF-8">
<title>Sérénité Bienveillante – Étiquette beurre de cacahuète</title>
<link href="https://fonts.googleapis.com/css2?family=Quicksand:wght@500;700&family=Poppins:wght@400;600;700&display=swap" rel="stylesheet">
<style>
  :root {
    --green: #349a7c;
    --green-dark: #2c8a6f;
    --mint: #e3f1ec;
    --ink: #1f2d2a;
    --white: #ffffff;
    --page: #ffffff;
  }
  * { box-sizing: border-box; margin: 0; padding: 0; }
  html, body { width: 1200px; height: 1000px; overflow: hidden; background: var(--page); }
  body { position: relative; font-family: "Poppins", sans-serif; color: var(--ink); }

  .label {
    position: absolute; left: 40px; top: 353px;
    width: 1120px; height: 294px;
    background: var(--white);
    box-shadow: 0 4px 10px rgba(0,0,0,0.18);
    overflow: hidden;
  }
  .pattern-area {
    position: absolute; left: 0; top: 41px; width: 100%; height: 231px;
    background: linear-gradient(180deg, var(--mint) 0%, #f3f9f7 50%, var(--mint) 100%);
    opacity: 0.7;
  }
  .top-band { position: absolute; left: 0; top: 0; width: 100%; height: 60px; }

  .center-panel {
    position: absolute; left: 429px; top: 94px; width: 260px; text-align: center;
  }
  .brand-name {
    font-family: "Quicksand", sans-serif; font-weight: 700;
    font-size: 21px; letter-spacing: 1px; color: var(--ink);
  }
  .brand-dot {
    display: inline-block; width: 10px; height: 10px; border-radius: 50%;
    background: var(--green); margin-right: 6px; vertical-align: 2px;
  }
  .product-title {
    margin-top: 16px;
    font-family: "Quicksand", sans-serif; font-weight: 700;
    font-size: 29px; line-height: 1; color: var(--green);
  }
  .product-subtitle {
    font-family: "Quicksand", sans-serif; font-weight: 700;
    font-size: 15.5px; line-height: 1.2; color: var(--ink);
  }
  .dose {
    width: 136px; margin: 5px auto 0; padding: 3px 0;
    border-top: 1.5px solid var(--green); border-bottom: 1.5px solid var(--green);
    font-family: "Quicksand", sans-serif; font-weight: 700; font-size: 15px;
  }
  .dose .cbd { color: var(--green); margin-right: 8px; }
  .for-dogs {
    margin-top: 12px; display: flex; justify-content: center; align-items: center; gap: 6px;
  }
  .for-dogs span {
    font-family: "Quicksand", sans-serif; font-weight: 700;
    font-size: 11px; line-height: 1; text-align: left; color: var(--ink);
  }
  .dog-icon {
    width: 26px; height: 34px; border-radius: 8px;
    background: linear-gradient(180deg, #d7ece5, #b8ddd0);
  }

  .dosage-table {
    position: absolute; left: 48px; top: 173px; width: 190px; height: 77px;
    border: 1.5px solid var(--green); border-radius: 4px; background: var(--white);
    overflow: hidden;
  }
  .dosage-table h3 {
    background: var(--green); color: var(--white);
    font-family: "Quicksand", sans-serif; font-weight: 700; font-size: 10px;
    padding: 3px 8px; height: 19px;
  }
  .dosage-table ul { list-style: none; padding: 5px 10px; }
  .dosage-table li {
    display: flex; align-items: center; height: 15.5px; font-size: 9.5px;
  }
  .dosage-table .size { width: 47px; font-weight: 700; color: var(--green-dark); font-size: 9px; }
  .dosage-table .scoops { display: flex; gap: 4px; margin-right: 5px; }
  .scoop-dot { width: 9px; height: 9px; border: 1.3px solid var(--green); border-radius: 50%; }
  .dosage-table .unit { color: var(--green); }

  .info-column { position: absolute; left: 818px; top: 58px; width: 248px; }
  .info-title {
    font-family: "Quicksand", sans-serif; font-weight: 700;
    font-size: 19.5px; color: var(--green); white-space: nowrap; text-align: center;
  }
  .info-lead {
    margin-top: 4px; font-size: 8.5px; line-height: 14px; text-align: justify;
  }
  .info-lead strong { color: var(--green); }
  .info-box {
    background: var(--green); color: var(--white); border-radius: 3px;
    font-size: 7.6px; line-height: 10px; text-align: justify;
    padding: 4px 10px; margin-top: 6px;
  }
  .info-box.first { margin-top: 11px; padding: 5px 10px; }
  .info-box strong { font-weight: 700; }

  .bottom-band {
    position: absolute; left: 0; top: 272px; width: 100%; height: 22px;
    background: var(--green); color: var(--white);
  }
  .claims {
    position: absolute; left: 0; width: 1120px; top: 3px; text-align: center;
    font-family: "Quicksand", sans-serif; font-weight: 700; font-size: 11.5px; letter-spacing: 0.3px;
  }
  .net-weight { position: absolute; right: 54px; top: 4px; font-size: 9.5px; }
  .net-weight strong { font-weight: 700; }
</style>
</head>
<body>
  <section class="label">
    <div class="pattern-area" role="img" aria-label="Motif d'os de chien en vert menthe pâle sur fond blanc"></div>

    <svg class="top-band" viewBox="0 0 1120 60" preserveAspectRatio="none" aria-hidden="true">
      <path d="M0 35 H530 Q552 35 559 54 Q566 35 588 35 H1120 V41 H590 Q570 41 559 60 Q548 41 528 41 H0 Z" fill="#349a7c"/>
    </svg>

    <div class="center-panel">
      <div class="brand-name"><span class="brand-dot"></span>VERDALYS</div>
      <h1 class="product-title">SÉRÉNITÉ</h1>
      <div class="product-subtitle">BIENVEILLANTE</div>
      <div class="dose"><span class="cbd">CBD</span>150 MG</div>
      <div class="for-dogs">
        <span>POUR<br>CHIENS</span>
        <div class="dog-icon" role="img" aria-label="Pictogramme de chien assis"></div>
      </div>
    </div>

    <div class="dosage-table">
      <h3>DOSAGE TABLE:</h3>
      <ul>
        <li><span class="size">PETIT:</span><span class="scoops"><i class="scoop-dot"></i></span><span class="unit">cuillère à café</span></li>
        <li><span class="size">MOYEN:</span><span class="scoops"><i class="scoop-dot"></i><i class="scoop-dot"></i></span><span class="unit">cuillère à café</span></li>
        <li><span class="size">GRAND:</span><span class="scoops"><i class="scoop-dot"></i><i class="scoop-dot"></i><i class="scoop-dot"></i></span><span class="unit">cuillère à café</span></li>
      </ul>
    </div>

    <div class="info-column">
      <h2 class="info-title">Tendre Comme Un Câlin</h2>
      <p class="info-lead">Enrichi en extrait de chanvre naturellement apaisant, le beurre de cacahuète <strong>NUTAVIA™</strong> est une délicieuse friandise d'occupation à lécher.</p>
      <p class="info-box first"><strong>UTILISATION:</strong> Laissez votre chien lécher cette gourmandise pour traverser en douceur les événements stressants du quotidien (absence, toilettage, trajet en voiture, etc.).</p>
      <p class="info-box"><strong>ASTUCE:</strong> Pour une utilisation optimale, étalez le beurre de cacahuète sur le tapis de léchage <strong>LICKORA™</strong>.</p>
      <p class="info-box"><strong>INGRÉDIENTS:</strong> Beurre de cacahuète, extrait de chanvre (0% THC).</p>
    </div>

    <div class="bottom-band">
      <div class="claims">ANTI-STRESS • 100% NATUREL • A LÉCHER • BEURRE DE CACAHUÈTE</div>
      <div class="net-weight"><strong>Poids Net:</strong> 250g</div>
    </div>
  </section>
</body>
</html>
```